Brenford Works Business Card

Modern and Professional Business Card for a Med size construction/development company.

See the samples below for the design I like … but I need ideas for incorporating the red company logo while still keeping the clean look of the card samples that are attached.

Logo and tag line on the back … info on the front.

Tagline: Quality Starts from the Ground Up

Target Market(s)

Med-Large General Contractors

Contact Information for Business Card

Brenford Works Limited
42 Marsh Lane
Mt. Pearl, NL
A1N 6T2

t: 709-555-0142
f: 709-555-0187
w: www.brenfordworks.example

Font styles to use
Sans Serif

Colors
fbee3e

Requirements
Must have
• I like the black and yellow designs of the attached samples …. but I'm not sure how to incorporate the red Brenford Works logo into that design??
Nice to have
• Construction safety strips

```html
<!DOCTYPE html>
<html lang="en">
<head>
<meta charset="utf-8">
<title>Brenford Works Business Card</title>
<link href="https://fonts.googleapis.com/css2?family=Montserrat:wght@400;500;600;700&display=swap" rel="stylesheet">
<style>
  :root {
    --stage: #1c1c1d;
    --card: #2b2b2c;
    --plate-light: #505053;
    --plate-dark: #343436;
    --plate-text: #d9d9db;
    --red: #e31e24;
    --yellow: #fbee3e;
    --white: #ffffff;
    --ink: #1e1e1f;
  }
  * { margin: 0; padding: 0; box-sizing: border-box; }
  html, body { width: 1200px; height: 878px; overflow: hidden; }
  body {
    background: var(--stage);
    font-family: "Montserrat", sans-serif;
    display: flex;
    align-items: center;
    justify-content: center;
    gap: 40px;
  }
  .card {
    position: relative;
    width: 540px;
    height: 309px;
    border-radius: 18px;
    background: var(--card);
    overflow: hidden;
    box-shadow: 0 14px 30px rgba(0,0,0,.45);
  }
  /* Back */
  .card-back {
    display: flex;
    flex-direction: column;
    align-items: center;
    justify-content: center;
    gap: 18px;
  }
  .back-plate {
    width: 260px;
    height: 104px;
    border-radius: 16px;
    background: linear-gradient(135deg, var(--plate-light), var(--plate-dark) 65%, #2e2e30);
    box-shadow: inset 0 1px 0 rgba(255,255,255,.12), 0 2px 6px rgba(0,0,0,.35);
    display: flex;
    align-items: center;
    justify-content: center;
  }
  .back-name {
    font-weight: 700;
    font-size: 19px;
    color: var(--plate-text);
    letter-spacing: .5px;
    text-align: center;
    line-height: 1.25;
  }
  .tagline {
    font-size: 12px;
    font-weight: 500;
    letter-spacing: 1.5px;
    text-transform: uppercase;
    color: var(--yellow);
  }
  /* Front */
  .front-band { position: absolute; inset: 0; }
  .front-logo {
    position: absolute;
    left: 34px;
    top: 92px;
    width: 228px;
    height: 104px;
    border-radius: 20px;
    background: var(--ink);
    padding: 8px;
  }
  .front-logo-inner {
    width: 100%;
    height: 100%;
    border-radius: 14px;
    background: var(--red);
    display: flex;
    align-items: center;
    justify-content: center;
  }
  .front-name {
    font-weight: 700;
    font-size: 19px;
    color: var(--ink);
    text-align: center;
    line-height: 1.25;
  }
  .details {
    position: absolute;
    left: 300px;
    top: 70px;
    color: var(--white);
  }
  .person { font-size: 21px; font-weight: 500; color: var(--red); letter-spacing: 1px; text-transform: uppercase; }
  .role { font-size: 12px; margin-top: 2px; }
  .address { font-size: 13px; line-height: 1.45; margin-top: 22px; }
  .contacts { list-style: none; margin-top: 20px; font-size: 13px; line-height: 1.6; }
  .contacts li { display: flex; align-items: center; gap: 8px; }
  .contacts svg { width: 10px; height: 10px; flex: none; }
</style>
</head>
<body>

  <section class="card card-back" aria-label="Card back">
    <div class="back-plate">
      <span class="back-name">BRENFORD WORKS<br>LIMITED</span>
    </div>
    <p class="tagline">Quality Starts from the Ground Up</p>
  </section>

  <section class="card card-front" aria-label="Card front">
    <svg class="front-band" viewBox="0 0 540 309" aria-hidden="true">
      <polygon points="0,0 186,0 118,309 0,309" fill="var(--red)"/>
      <polygon points="190,0 196,0 128,309 122,309" fill="var(--white)"/>
    </svg>

    <div class="front-logo">
      <div class="front-logo-inner">
        <span class="front-name">BRENFORD WORKS<br>LIMITED</span>
      </div>
    </div>

    <div class="details">
      <p class="person">Daniel Archer</p>
      <p class="role">Director</p>
      <p class="address">42 Marsh Lane<br>Mt. Pearl, NL A1N 6T2</p>
      <ul class="contacts">
        <li>
          <svg viewBox="0 0 10 10" aria-hidden="true"><path d="M2 1 L4 1 L4.6 3 L3.5 4 Q4.5 6 6 6.5 L7 5.4 L9 6 L9 8 Q8 9 6.5 8.6 Q2 7 1.2 2.6 Q1.2 1.4 2 1Z" fill="var(--red)"/></svg>
          709-555-0142
        </li>
        <li>
          <svg viewBox="0 0 10 10" aria-hidden="true"><rect x="2.5" y="0.5" width="5" height="9" rx="1" fill="none" stroke="var(--red)" stroke-width="1.1"/><circle cx="5" cy="7.8" r=".6" fill="var(--red)"/></svg>
          709-555-0187
        </li>
        <li>
          <svg viewBox="0 0 10 10" aria-hidden="true"><rect x=".6" y="2" width="8.8" height="6" fill="none" stroke="var(--red)" stroke-width="1"/><path d="M.8 2.3 L5 5.6 L9.2 2.3" fill="none" stroke="var(--red)" stroke-width="1"/></svg>
          info@brenfordworks.example
        </li>
        <li>
          <svg viewBox="0 0 10 10" aria-hidden="true"><circle cx="5" cy="5" r="4.2" fill="none" stroke="var(--red)" stroke-width="1"/><ellipse cx="5" cy="5" rx="1.8" ry="4.2" fill="none" stroke="var(--red)" stroke-width=".8"/><path d="M.8 5 H9.2" stroke="var(--red)" stroke-width=".8"/></svg>
          www.brenfordworks.example
        </li>
      </ul>
    </div>
  </section>

</body>
</html>
```